Digitales Briefpapier für IT-Systemhaus
Zielgruppe
IT-Systemhaus mit dem Schwerpunkt Digitalisierung von Geschäftsprozessen. Ggf. Schlagwörter wie DMS, ECM, Digitalisierung Ihrer Prozesse unterbringen.
Aufgabenstellung
Digitale Vorlage (Word) um daraus dann ein PDF zu generieren. Anschrift usw. auf QXN.de

```html
<!DOCTYPE html>
<html lang="de">
<head>
<meta charset="utf-8">
<title>QXN.de Briefpapier</title>
<link rel="stylesheet" href="https://fonts.googleapis.com/css2?family=Jura:wght@400;500&display=swap">
<style>
  :root {
    --backdrop: #9c9c9c;
    --paper: #ffffff;
    --brand-blue: #3163a6;
    --accent-blue: #5f86c8;
    --text-grey: #5a5a5a;
    --rule-grey: #c8c8c8;
  }
  * { margin: 0; padding: 0; box-sizing: border-box; }
  html, body {
    width: 847px; height: 1200px; overflow: hidden;
    background: var(--backdrop);
    font-family: "Jura", "Helvetica Neue", Arial, sans-serif;
  }
  .letterhead {
    position: absolute; left: 53px; top: 76px;
    width: 741px; height: 1047px;
    background: var(--paper);
  }
  .header-band {
    position: absolute; left: 0; top: 0; width: 741px; height: 100px;
    background: var(--brand-blue);
  }
  .tagline {
    position: absolute; left: 56px; top: 49px;
    color: #fff; font-size: 8.6px; font-weight: 500;
  }
  .company-name {
    position: absolute; right: 36px; top: 34px;
    color: #fff; font-size: 30px; font-weight: 500;
    letter-spacing: 0; line-height: 1;
  }
  .return-address {
    position: absolute; left: 107px; top: 157px;
    font-size: 6.4px; color: var(--text-grey); white-space: nowrap;
  }
  .return-address .company { color: var(--accent-blue); }
  .return-address .sep { margin: 0 3px; }
  .sender-block {
    position: absolute; left: 537px; top: 136px;
    font-size: 11px; line-height: 13.4px; color: var(--text-grey);
    font-style: normal;
  }
  .sender-block .company, .label { color: var(--accent-blue); }
  .sender-block .contact { margin-top: 5px; }
  .fold-mark { position: absolute; left: 26px; width: 5px; height: 8px; }
  .fold-mark.upper { top: 390px; }
  .fold-mark.lower { top: 665px; }
  .footer-rule {
    position: absolute; left: 89px; top: 961px; width: 570px;
    border-top: 1px solid var(--rule-grey);
  }
  .footer-col {
    position: absolute; top: 972px;
    font-size: 10.5px; line-height: 13.9px; color: var(--text-grey);
  }
  .footer-col .heading { color: var(--accent-blue); }
  .footer-col.company-info { left: 89px; }
  .footer-col.management { left: 323px; }
  .footer-col.banking { left: 456px; }
  .footer-col.banking .heading { color: var(--text-grey); }
</style>
</head>
<body>
  <div class="letterhead">
    <header class="header-band">
      <p class="tagline">DMS, ECM, Digitalisierung Ihrer Prozesse unterbringen.</p>
      <p class="company-name">QXN.de</p>
    </header>

    <p class="return-address"><span class="company">QXN.de Systemhaus GmbH &amp; Co. KG</span><span class="sep">•</span>Lindenhofweg 12b<span class="sep">•</span>29410 Wiesenau</p>

    <address class="sender-block">
      <div class="company">QXN.de Systemhaus GmbH &amp; Co. KG</div>
      <div>Lindenhofweg 12b</div>
      <div>29410 Wiesenau</div>
      <div class="contact"><span class="label">Tel.</span>&nbsp;&nbsp; +49 (555) 0184200</div>
      <div><span class="label">Fax.</span>&nbsp; +49 (555) 01842333</div>
      <div>info(at)qxn.de</div>
      <div>www.qxn.de</div>
    </address>

    <svg class="fold-mark upper" viewBox="0 0 5 8" aria-hidden="true"><path d="M0 0 L5 4 L0 8 Z" fill="var(--brand-blue)"/></svg>
    <svg class="fold-mark lower" viewBox="0 0 5 8" aria-hidden="true"><path d="M0 0 L5 4 L0 8 Z" fill="var(--brand-blue)"/></svg>

    <div class="footer-rule"></div>
    <footer>
      <div class="footer-col company-info">
        <div class="heading">QXN.de Systemhaus GmbH &amp; Co. KG</div>
        <div>Lindenhofweg 12b</div>
        <div>29410 Wiesenau</div>
      </div>
      <div class="footer-col management">
        <div class="heading">Geschäftsführer</div>
        <div>Max Mustermann</div>
        <div>Sitz:&nbsp; Mustermann</div>
        <div>USt:&nbsp; DE091XXXX</div>
      </div>
      <div class="footer-col banking">
        <div class="heading">Bankverbindung</div>
        <div>Hansa Regionalbank</div>
        <div>Bic: HRBKDE21XXX</div>
        <div>IBAN: DE17 XX00 0250 XXX 0377 19</div>
      </div>
    </footer>
  </div>
</body>
</html>
```